Kelmora Legal Business Card

I require a corporate business card for a new legal services business.

I do not have a logo, nor do I want one.

I require a clean, neat a professional card for a law firm.

Details:

Business Name: Kelmora Legal
Name: Debra Lindqvist
Title: Corporate Services Manager
Location: Office 14 (Top Floor), Toravel Business Centre, Quinlan Grove Street, Alotau CBD, Milne Bay Province.
Postal Address: PO Box 593, Alotau, 211, Milne Bay Province, Papua New Guinea.
Contact: T: +675 6418250, F: +675 6413362, M: +675 72915867, E: dlindqvist@kelmoraexample.com.pg.

I look forward to your design submissions.

Industry/Entity Type

Legal

```html
<!DOCTYPE html>
<html lang="en">
<head>
<meta charset="utf-8">
<title>Kelmora Legal Business Card</title>
<link href="https://fonts.googleapis.com/css2?family=Exo+2:wght@400;500&family=Roboto:wght@300;400&display=swap" rel="stylesheet">
<style>
  :root {
    --page: #e9e7e3;
    --card: #ffffff;
    --brand: #2f55b5;
    --ink: #2b2f36;
    --muted: #5b6068;
    --band-light: #3a8fdc;
    --band-dark: #2247a8;
    --swoosh: #3a3d44;
  }
  * { margin: 0; padding: 0; box-sizing: border-box; }
  html, body { width: 1200px; height: 828px; overflow: hidden; }
  body {
    background: var(--page);
    font-family: "Roboto", Arial, sans-serif;
    position: relative;
  }
  .card {
    position: absolute;
    top: 269px;
    width: 500px;
    height: 290px;
    background: var(--card);
    box-shadow: 0 6px 18px rgba(0,0,0,0.12);
    overflow: hidden;
  }
  .card--front { left: 70px; }
  .card--back { left: 630px; }

  .wordmark {
    font-family: "Exo 2", Arial, sans-serif;
    font-weight: 500;
    color: var(--brand);
    letter-spacing: 0.5px;
    white-space: nowrap;
  }
  .card--front .wordmark {
    position: absolute;
    left: 0; right: 0; top: 118px;
    text-align: center;
    font-size: 44px;
  }
  .card--back .wordmark {
    position: absolute;
    left: 34px; top: 92px;
    font-size: 40px;
  }

  .holder {
    position: absolute;
    right: 30px; top: 34px;
    text-align: right;
    color: var(--ink);
  }
  .holder__name { font-size: 12px; letter-spacing: 1px; }
  .holder__title { font-size: 8px; color: var(--muted); margin-top: 2px; }

  .address {
    position: absolute;
    right: 30px; top: 88px;
    text-align: right;
    font-size: 9px;
    line-height: 14px;
    color: var(--ink);
  }

  .contacts {
    position: absolute;
    left: 40px; top: 172px;
    list-style: none;
    font-size: 10px;
    color: var(--ink);
  }
  .contacts li {
    display: flex;
    align-items: center;
    height: 18px;
  }
  .contacts svg { width: 10px; height: 10px; margin-right: 8px; fill: var(--ink); }

  .band {
    position: absolute;
    left: 0; top: 0;
    width: 500px; height: 290px;
  }
  .website {
    position: absolute;
    left: 428px; top: 250px;
    font-size: 8.5px;
    letter-spacing: 0.8px;
    color: #ffffff;
    white-space: nowrap;
    transform: translate(-50%, -50%) rotate(-25deg);
  }
</style>
</head>
<body>

  <section class="card card--front" aria-label="Card front">
    <div class="wordmark">Kelmora Legal</div>
  </section>

  <section class="card card--back" aria-label="Card back">
    <svg class="band" viewBox="0 0 500 290" aria-hidden="true">
      <defs>
        <linearGradient id="bandFill" x1="0" y1="1" x2="1" y2="0">
          <stop offset="0" stop-color="var(--band-dark)"/>
          <stop offset="1" stop-color="var(--band-light)"/>
        </linearGradient>
      </defs>
      <path d="M170 290 C 280 270, 400 215, 500 150 L 500 290 Z" fill="var(--swoosh)"/>
      <path d="M200 290 C 300 272, 410 225, 500 166 L 500 290 Z" fill="url(#bandFill)"/>
    </svg>

    <div class="wordmark">Kelmora Legal</div>

    <div class="holder">
      <div class="holder__name">DEBRA LINDQVIST</div>
      <div class="holder__title">Corporate Services Manager</div>
    </div>

    <div class="address">
      Office 14, Quinlan Grove St<br>
      Alotau, Milne Bay
    </div>

    <ul class="contacts">
      <li>
        <svg viewBox="0 0 10 10"><path d="M2 0.5 L3.8 2.6 L2.9 3.6 C3.5 4.9 5 6.4 6.4 7.1 L7.4 6.2 L9.5 8 L8.3 9.5 C4.5 9.3 0.7 5.5 0.5 1.7 Z"/></svg>
        +675 6418250
      </li>
      <li>
        <svg viewBox="0 0 10 10"><path d="M2.5 0 H7.5 V10 H2.5 Z M3.3 1 V8 H6.7 V1 Z"/></svg>
        +675 72915867
      </li>
      <li>
        <svg viewBox="0 0 10 10"><path d="M2 0 H8 V3 H2 Z M0.5 3.5 H9.5 V8 H8 V10 H2 V8 H0.5 Z M3 6.5 V9 H7 V6.5 Z"/></svg>
        +675 6413362
      </li>
      <li>
        <svg viewBox="0 0 10 10"><path d="M0.5 2 H9.5 V8.5 H0.5 Z M1.2 2.6 L5 5.6 L8.8 2.6 Z"/></svg>
        dlindqvist@kelmoraexample.com.pg
      </li>
    </ul>

    <div class="website">www.kelmoraexample.com.pg</div>
  </section>

</body>
</html>
```